Business card - house cleaning company

We want friendly high end business card highlighting our services . NO LOGOs on back of card please.. no vertical cards NO DOUBLE BROOMS

2 owners of the company: Corinne Halvey & Joel Brandt

Included phone number: (555)318-2047

Email: brightlanetidy@mailnest.example

Website: www.brightlanetidy.example

Bonded & Insured

Larkspur Bend, CO 80000

Slogan maybe: Bringing a brighter shine to every corner of home

We want elegant high end card for house cleaning service. Maybe 2 sided if needed. Can it have bullet points of some services we offer

Residential Home Cleaning
Vacation Rental Cleaning
Commercial Cleaning
Carpet Cleaning
Window Cleaning
Property Management
Property Inspections
Property Maintenance
Trash Removal
Concierge Services

Highlight service on back of card. If we can do a one sided card with all this that’s great as well. Not cartoony.

Our logo attached and a design somone I had Perrin but they put very little time in. Not Unique enough. If you can do a custom design with a feminine touch that be great.

You will be eliminated for not reading the brief. NO DOUBLE LOGOS NO DOUBLE BROOMS. PLEASE BE CREATIVE. IF POST SAME LOGO WITH SMAL CHANGES RHEY WILL BE ELIMINATED. BE CREATIVE.

Thank you everyone for your designs. please only use the logo 1 time. and would love to see some that dont look all the same. We appreciate your time.

Target Market(s)

Residential and vacation rental home cleaning maid service

Industry/Entity Type

House cleaning maid services

Contact Information for Business Card

For business card use logo. black and green one provided. others for example. I wil try find some example.. We want friendly high end look. 2 owners of the company: Corinne Halvey & Joel Brandt Included phone number: (555)318-2047 Email: brightlanetidy@mailnest.example Website: www.brightlanetidy.example Bonded & Insured Estes Park, CO Slogan maybe: Bringing a brighter shine to every corner of home or Quality Service Guaranteed We want elegant high end card for house cleaning service. Maybe 2 sided if needed. Can it have bullet points of some services we offer Residential Home Cleaning Vacation Rental Cleaning Commercial Cleaning Carpet Cleaning Window Cleaning Property Management Property Inspections Property Maintenance Trash Removal Concierge Services

Requirements
Must have
• For business card use logo . Creativity. black and green one provided. We want friendly high end look. 2 owners of the company: Corinne Halvey & Joel Brandt Included phone number: (555)318-2047 Email: brightlanetidy@mailnest.example Website: www.brightlanetidy.example Licensed Bonded & Insured Estes Park, CO Slogan maybe: Bringing a brighter shine to every corner of home or Quality Service Guaranteed We want elegant high end card for house cleaning service. Maybe 2 sided if needed. Can it have bullet points of some services we offer Residential Home Cleaning Vacation Rental Cleaning Commercial Cleaning Carpet Cleaning Window Cleaning Property Management Property Inspections Property Maintenance Trash Removal Concierge Services .. creatitivty a plus. whimsical. we like stars..
Nice to have
• we want much better than the example of biz card provided as example. logo has colors that are in our website palette as well. We are open to ideas for the business card design. Will pay tip to best work. PLEASE USE COMPLIMENTING COLORS. . WE LIKE BLACK AND WHITE, stars
Should not have
• NO DOUBLE LOGOS. READ READ. READ. YOU WILL BE ELIMINATED no double logos or double brooms same side of card. I want didfrent examples. please don't make all your submission look the same

```html
<!DOCTYPE html>
<html lang="en">
<head>
<meta charset="utf-8">
<title>Brightlane Cleaning Services – Business Card</title>
<link href="https://fonts.googleapis.com/css2?family=Gilda+Display&family=Allura&display=swap" rel="stylesheet">
<style>
  :root{
    --stage:#2e2b2a;
    --card-black:#000000;
    --band:#1b1b1b;
    --green:#6f9b45;
    --green-light:#8cc05a;
    --white:#ffffff;
    --rule:#5a5a5a;
  }
  *{margin:0;padding:0;box-sizing:border-box}
  html,body{width:975px;height:1200px;overflow:hidden;background:var(--stage)}
  body{position:relative;font-family:"Gilda Display",Georgia,serif;color:var(--white)}
  .card{
    position:absolute;left:87px;width:806px;height:483px;overflow:hidden;
    background:
      radial-gradient(ellipse 340px 150px at 50% 0%, rgba(140,138,140,.55), rgba(60,60,62,.2) 60%, transparent 100%),
      linear-gradient(180deg,#2a2a2c 0%,#141416 45%,var(--card-black) 80%);
    box-shadow:0 10px 30px rgba(0,0,0,.45);
  }
  .card--front{top:84px}
  .card--back{top:624px;left:88px}
  .band{position:absolute;left:0;width:100%;height:32px;background:var(--band);
    display:flex;align-items:center;justify-content:center;gap:12px}
  .band-foot{position:absolute;left:0;bottom:0;width:100%;background:var(--card-black)}
  .brand{position:absolute;top:58px;left:0;width:100%;text-align:center;color:var(--white)}
  .brand-name{display:block;font-size:66px;line-height:1;letter-spacing:-1px}
  .brand-sub{display:block;font-size:21px;letter-spacing:1.5px;text-transform:uppercase;margin-top:6px}
  .tagline-block{position:absolute;border-top:1px solid var(--rule);border-bottom:1px solid var(--rule);
    display:flex;align-items:center;justify-content:center}
  .tagline{font-family:"Allura",cursive;color:var(--green-light);white-space:nowrap}
  .front-tagline{left:198px;top:197px;width:409px;height:44px}
  .front-tagline .tagline{font-size:26px}
  .owners{position:absolute;left:0;width:100%;text-align:center;font-size:24px}
  .phone-row{position:absolute;left:0;top:300px;width:100%;display:flex;justify-content:center;align-items:center;gap:6px;font-size:30px}
  .icon{display:inline-flex;align-items:center;justify-content:center;border-radius:50%;background:var(--green)}
  .contact-row{position:absolute;left:0;top:354px;width:100%;display:flex;justify-content:center;align-items:center;font-size:17px}
  .contact-row .icon{margin-right:14px}
  .divider{margin:0 22px}
  .band-text{font-size:14.5px;letter-spacing:1.5px;text-transform:uppercase}
  .back-tagline{left:272px;top:79px;width:261px;height:51px}
  .back-tagline .tagline{font-size:26px}
  .services{position:absolute;top:166px;list-style:none}
  .services li{position:relative;height:34.5px;font-size:17px;padding-left:24px;white-space:nowrap}
  .services li svg{position:absolute;left:0;top:4px}
  .services--left{left:135px}
  .services--right{left:480px}
  .back-band-text{font-size:17px}
</style>
</head>
<body>

<section class="card card--front">
  <div class="brand">
    <span class="brand-name">Brightlane</span>
    <span class="brand-sub">Cleaning Services</span>
  </div>

  <div class="tagline-block front-tagline">
    <span class="tagline">Bringing a brighter shine to every corner of home</span>
  </div>

  <p class="owners" style="top:257px">Corinne Halvey &amp; Joel Brandt</p>

  <div class="phone-row">
    <span class="icon" style="width:34px;height:34px">
      <svg width="14" height="20" viewBox="0 0 14 20"><rect x="1" y="1" width="12" height="18" rx="2" fill="none" stroke="#fff" stroke-width="1.6"/><line x1="5" y1="16" x2="9" y2="16" stroke="#fff" stroke-width="1.4"/></svg>
    </span>
    <span>(555)318-2047</span>
  </div>

  <div class="contact-row">
    <span class="icon" style="width:23px;height:23px">
      <svg width="13" height="13" viewBox="0 0 14 14"><circle cx="7" cy="7" r="6" fill="none" stroke="#fff" stroke-width="1.2"/><ellipse cx="7" cy="7" rx="2.6" ry="6" fill="none" stroke="#fff" stroke-width="1"/><line x1="1" y1="7" x2="13" y2="7" stroke="#fff" stroke-width="1"/></svg>
    </span>
    <span>www.brightlanetidy.example</span>
    <span class="divider">|</span>
    <span class="icon" style="width:23px;height:23px">
      <svg width="13" height="10" viewBox="0 0 14 10"><rect x="1" y="1" width="12" height="8" fill="none" stroke="#fff" stroke-width="1.2"/><polyline points="1,1 7,6 13,1" fill="none" stroke="#fff" stroke-width="1.2"/></svg>
    </span>
    <span>brightlanetidy@mailnest.example</span>
  </div>

  <div class="band" style="top:398px">
    <svg width="10" height="14" viewBox="0 0 10 14"><path d="M5 0a5 5 0 0 1 5 5c0 3.6-5 9-5 9S0 8.6 0 5a5 5 0 0 1 5-5z" fill="#fff"/><circle cx="5" cy="5" r="1.8" fill="#1b1b1b"/></svg>
    <span class="band-text">Bonded &amp; Insured</span>
    <span class="band-text">|</span>
    <span class="band-text">Larkspur Bend, CO 80000</span>
  </div>
  <div class="band-foot" style="top:430px"></div>
</section>

<section class="card card--back">
  <div class="tagline-block back-tagline">
    <span class="tagline">Quality Service Guaranteed</span>
  </div>

  <ul class="services services--left">
    <li><svg width="14" height="14" viewBox="0 0 14 14"><path d="M7 0v14M0 7h14" stroke="#8cc05a" stroke-width="1.3"/></svg>Residential Home Cleaning</li>
    <li><svg width="14" height="14" viewBox="0 0 14 14"><path d="M7 0v14M0 7h14" stroke="#8cc05a" stroke-width="1.3"/></svg>Vacation Rental Cleaning</li>
    <li><svg width="14" height="14" viewBox="0 0 14 14"><path d="M7 0v14M0 7h14" stroke="#8cc05a" stroke-width="1.3"/></svg>Commercial Cleaning</li>
    <li><svg width="14" height="14" viewBox="0 0 14 14"><path d="M7 0v14M0 7h14" stroke="#8cc05a" stroke-width="1.3"/></svg>Carpet Cleaning</li>
    <li><svg width="14" height="14" viewBox="0 0 14 14"><path d="M7 0v14M0 7h14" stroke="#8cc05a" stroke-width="1.3"/></svg>Window Cleaning</li>
  </ul>

  <ul class="services services--right">
    <li><svg width="14" height="14" viewBox="0 0 14 14"><path d="M7 0v14M0 7h14" stroke="#8cc05a" stroke-width="1.3"/></svg>Property Management</li>
    <li><svg width="14" height="14" viewBox="0 0 14 14"><path d="M7 0v14M0 7h14" stroke="#8cc05a" stroke-width="1.3"/></svg>Property Inspections</li>
    <li><svg width="14" height="14" viewBox="0 0 14 14"><path d="M7 0v14M0 7h14" stroke="#8cc05a" stroke-width="1.3"/></svg>Property Maintenance</li>
    <li><svg width="14" height="14" viewBox="0 0 14 14"><path d="M7 0v14M0 7h14" stroke="#8cc05a" stroke-width="1.3"/></svg>Trash Removal</li>
    <li><svg width="14" height="14" viewBox="0 0 14 14"><path d="M7 0v14M0 7h14" stroke="#8cc05a" stroke-width="1.3"/></svg>Concierge Services</li>
  </ul>

  <div class="band" style="top:394px">
    <span class="back-band-text">Corinne Halvey &amp; Joel Brandt</span>
    <span class="icon" style="width:26px;height:26px;margin-left:4px">
      <svg width="10" height="15" viewBox="0 0 14 20"><rect x="1" y="1" width="12" height="18" rx="2" fill="none" stroke="#fff" stroke-width="1.8"/><line x1="5" y1="16" x2="9" y2="16" stroke="#fff" stroke-width="1.6"/></svg>
    </span>
    <span class="back-band-text" style="margin-left:-8px">(555)318-2047</span>
  </div>
  <div class="band-foot" style="top:426px"></div>
</section>

</body>
</html>
```